Torvale Wound Care Business card design

We need a business card designed around our logo which was provided. The logo of preference is the colored. Also the colors and fonts were provided.

Target Market(s)

Our Referral partners are home health agencies.

Industry/Entity Type

Healthcare

Contact Information for Business Card

Name , Phone #, Email , Title

Requirements
Nice to have
• Creativity
Should not have
• basic

```html
<!DOCTYPE html>
<html lang="en">
<head>
<meta charset="utf-8">
<title>Torvale Wound Care – Business Card</title>
<link href="https://fonts.googleapis.com/css2?family=Tinos:wght@400;700&family=Montserrat:wght@400&display=swap" rel="stylesheet">
<style>
  :root {
    --bg: #232323;
    --navy: #2e3a8f;
    --royal: #1f5fb5;
    --sky: #00aeef;
    --white: #ffffff;
    --ink: #2a2a2a;
    --rule: #4a4a4a;
  }
  * { margin: 0; padding: 0; box-sizing: border-box; }
  html, body {
    width: 1200px; height: 800px; overflow: hidden;
    background: var(--bg);
  }
  .stage {
    position: relative; width: 1200px; height: 800px;
  }
  .card {
    position: absolute; top: 245px;
    width: 540px; height: 310px;
    border-radius: 28px; overflow: hidden;
    box-shadow: 0 18px 30px rgba(0,0,0,0.45);
  }
  .card--front {
    left: 40px;
    background: linear-gradient(225deg, var(--sky) 0%, var(--royal) 50%, var(--navy) 100%);
    display: flex; align-items: center; justify-content: center;
  }
  .card--back {
    left: 620px;
    background: var(--white);
  }
  .brand {
    display: flex; align-items: center; gap: 14px;
  }
  .brand__mark {
    width: 34px; height: 34px; border-radius: 6px;
  }
  .brand__name {
    font-family: "Tinos", serif; font-weight: 700;
    white-space: nowrap;
  }
  .card--front .brand__mark { background: var(--white); }
  .card--front .brand__name { color: var(--white); font-size: 40px; }

  .card--back .brand {
    position: absolute; top: 36px; right: 36px; gap: 10px;
  }
  .card--back .brand__mark { width: 22px; height: 22px; border-radius: 4px; background: var(--royal); }
  .card--back .brand__name { color: var(--navy); font-size: 24px; }

  .holder {
    position: absolute; left: 40px; top: 142px;
  }
  .holder__name {
    font-family: "Tinos", serif; font-weight: 700;
    font-size: 22px; letter-spacing: 0.5px; text-transform: uppercase;
    color: var(--navy);
  }
  .holder__title {
    font-family: "Montserrat", sans-serif; font-size: 15px;
    color: var(--ink); margin-top: 4px;
  }
  .address {
    position: absolute; right: 36px; top: 150px; text-align: right;
    font-family: "Tinos", serif; font-size: 13px; line-height: 1.35;
    color: var(--ink);
  }
  .divider {
    position: absolute; left: 40px; right: 36px; top: 200px;
    height: 1px; background: var(--rule);
  }
  .contacts {
    position: absolute; left: 40px; top: 212px; list-style: none;
    font-family: "Tinos", serif; font-size: 14px; color: var(--ink);
  }
  .contacts__item {
    display: flex; align-items: center; gap: 10px; height: 22px;
  }
  .contacts__icon { width: 15px; height: 15px; flex: none; }
  .band {
    position: absolute; left: 0; bottom: 0; width: 540px; height: 40px;
  }
</style>
</head>
<body>
<main class="stage">

  <section class="card card--front" aria-label="Card front">
    <div class="brand">
      <span class="brand__mark"></span>
      <span class="brand__name">Torvale Wound Care</span>
    </div>
  </section>

  <section class="card card--back" aria-label="Card back">
    <div class="brand">
      <span class="brand__mark"></span>
      <span class="brand__name">Torvale Wound Care</span>
    </div>

    <div class="holder">
      <p class="holder__name">Daniel Harlow</p>
      <p class="holder__title">Owner</p>
    </div>

    <p class="address">421, Address line goes here<br>45452, Country name</p>

    <div class="divider"></div>

    <ul class="contacts">
      <li class="contacts__item">
        <svg class="contacts__icon" viewBox="0 0 16 16" aria-hidden="true">
          <path fill="#1f5fb5" d="M3.6 1.5l2.3 2.6-1.3 1.6c.9 2 2.4 3.6 4.4 4.6l1.6-1.3 2.6 2.2-1.3 2.3C7 13.3 2.6 8.9 1.5 2.8z"/>
        </svg>
        <span>0400 555 018</span>
      </li>
      <li class="contacts__item">
        <svg class="contacts__icon" viewBox="0 0 16 16" aria-hidden="true">
          <rect x="1" y="3.5" width="14" height="9.5" rx="1" fill="#1f5fb5"/>
          <path d="M1.5 4l6.5 5 6.5-5" fill="none" stroke="#ffffff" stroke-width="1.3"/>
        </svg>
        <span>info@torvalecare.com</span>
      </li>
      <li class="contacts__item">
        <svg class="contacts__icon" viewBox="0 0 16 16" aria-hidden="true">
          <circle cx="8" cy="8" r="7" fill="#1f5fb5"/>
          <ellipse cx="8" cy="8" rx="3" ry="7" fill="none" stroke="#ffffff" stroke-width="1"/>
          <path d="M1 8h14" stroke="#ffffff" stroke-width="1"/>
        </svg>
        <span>www.torvalecare.com</span>
      </li>
    </ul>

    <svg class="band" viewBox="0 0 540 40" preserveAspectRatio="none" aria-hidden="true">
      <defs>
        <linearGradient id="bandFill" x1="0" y1="0" x2="1" y2="0">
          <stop offset="0" stop-color="#2e3a8f"/>
          <stop offset="0.55" stop-color="#1f6fc5"/>
          <stop offset="1" stop-color="#00aeef"/>
        </linearGradient>
      </defs>
      <polygon points="0,34 300,34 312,20 540,20 540,40 0,40" fill="url(#bandFill)"/>
      <polygon points="312,20 322,20 310,34 300,34" fill="#ffffff"/>
    </svg>
  </section>

</main>
</body>
</html>
```